Slide Template Design - For Professional Powerpoint Presentation

Hello, this competition is to design one or more PowerPoint slides using the template provided as a base.

This presentation will be used by my business - to provide REPORTS (with lots of content on each slide) on investments to clients.

It is possible to win this competition by just designing 1 slide - the "Typical Slide (with Text)" is the most important.

The slides I would like are:
- Cover Page Template
- Table of Contents Template
- Section Divider Template
- Typical Slide (with Text)

The presentation should look clean, clear, highly professional, and use mainly black, grey, white colours. One colour may (but does not have to) feature as a design element.

The design is what I am most interested in - the text can be pasted in.

I do not need a logo (I already have on in black and white).

```html
<!DOCTYPE html>
<html lang="en">
<head>
<meta charset="UTF-8">
<title>Cover Slide Template</title>
<link href="https://fonts.googleapis.com/css2?family=Arimo:ital@1&family=Carlito:wght@400;700&family=Tinos&display=swap" rel="stylesheet">
<style>
  :root {
    --bg-dark: #2b2b2b;
    --bg-mid: #4a4a4a;
    --bg-light: #8a8a8a;
    --white: #ffffff;
    --black: #000000;
    --ink: #3a3a3a;
    --accent: #f05a1a;
  }
  html, body {
    margin: 0;
    padding: 0;
    width: 1200px;
    height: 675px;
    overflow: hidden;
    background: var(--bg-dark);
  }
  .slide {
    position: relative;
    width: 1200px;
    height: 675px;
    overflow: hidden;
  }
  .backdrop {
    position: absolute;
    inset: 0;
    background:
      radial-gradient(ellipse at 45% 55%, var(--bg-light) 0%, rgba(138,138,138,0) 45%),
      linear-gradient(135deg, var(--bg-dark) 0%, var(--bg-mid) 45%, var(--bg-dark) 100%);
  }
  .frame {
    position: absolute;
    left: 492px;
    top: 61px;
    width: 620px;
    height: 456px;
    border: 2px solid var(--white);
    box-sizing: border-box;
  }
  .logo-block {
    position: absolute;
    left: 612px;
    top: 93px;
    width: 344px;
    height: 148px;
    background: var(--black);
    box-shadow: 5px 5px 0 var(--white);
    color: var(--white);
    font-family: "Carlito", sans-serif;
    font-weight: 400;
    text-align: center;
    display: flex;
    flex-direction: column;
    justify-content: center;
    line-height: 1.2;
  }
  .logo-block .logo-line { font-size: 25px; }
  .logo-block .logo-main { font-size: 38px; }
  .title-card {
    position: absolute;
    left: 541px;
    top: 296px;
    width: 520px;
    height: 177px;
    background: var(--white);
    box-sizing: border-box;
    padding: 45px 0 0 27px;
    font-family: "Carlito", sans-serif;
    color: var(--ink);
    font-size: 28px;
  }
  .title-card p { margin: 0 0 19px; line-height: 1.2; }
  .page-number {
    position: absolute;
    left: 1097px;
    top: 291px;
    width: 103px;
    height: 93px;
    background: var(--accent);
    color: var(--white);
    font-family: "Tinos", serif;
    font-size: 22px;
    display: flex;
    align-items: center;
    justify-content: center;
  }
  .footer-text {
    position: absolute;
    top: 545px;
    font-family: "Arimo", sans-serif;
    font-style: italic;
    font-size: 35px;
    color: var(--white);
    margin: 0;
  }
  .date { left: 81px; }
  .tagline { left: 544px; }
</style>
</head>
<body>
  <div class="slide">
    <div class="backdrop" role="img" aria-label="Black and white photograph looking up at city skyscrapers"></div>
    <div class="frame"></div>
    <div class="logo-block">
      <span class="logo-line">Logo</span>
      <span class="logo-main">(do not design)</span>
      <span class="logo-line">Pty Ltd</span>
    </div>
    <div class="title-card">
      <p class="presentation-title">Presentation Title</p>
      <p class="presentation-description">Presentation Description</p>
    </div>
    <div class="page-number">01</div>
    <p class="footer-text date">date</p>
    <p class="footer-text tagline">"company tag line goes here"</p>
  </div>
</body>
</html>
```